Asphalt Paving Specialists Business Cards

Our company is TREVIN ASPHALT. We need a business cards two of our asphalt paving team members. We're asphalt specialists.
I need two made up please. The details on the front of the each business card i would like please is as follows.
Address is 87 Marrowby St, Clontarf, QLD, 4019.

Company Director
Gordon Pelliway
gord@trevinpave.com.au
04 58 736 042
www.trevinpave.com.au

Supervisor
Curtis Vonnegard
curtis@trevinpave.com.au
0462 873 105
www.trevinpave.com.au

We do all aspects of Asphalt Paving. Specific Services include - Driveways, Carparks & sub-divisions. All Roads. Repairs and Maintenance.

We provide free quotes!

I dont have a certain way i want them to look so im open to all designs :)

** I have uploaded our logo for the TREVIN ASPHALT. HOWEVER, CAN YOU PLEASE GET RID OF THE ( PTY LTD )

Thank you
Renata Fulch
TREVIN ASPHALT

Target Market(s)

Home owners and Business Owners

Contact Information for Business Card

Asphalt Paving Specialists. All aspects of Asphalt. Residential, Commercial & Industrial. Based in Brisbane.

Font styles to use
Sans Serif

Colors

Designer to choose colors to be used in the design.

Requirements
Nice to have
• maybe an image of a driveway? or Asphalt?

```html
<!DOCTYPE html>
<html lang="en">
<head>
<meta charset="utf-8">
<title>Trevin Asphalt – Business Card</title>
<link rel="stylesheet" href="https://fonts.googleapis.com/css2?family=Roboto:wght@400;500&family=Roboto+Condensed:wght@700&display=swap">
<style>
  :root {
    --page-bg: #d8d8d8;
    --card-dark: #000000;
    --card-light: #ffffff;
    --accent-blue: #0ea2dc;
    --text-white: #ffffff;
    --text-grey: #555555;
    --logo-ink: #111111;
    --rule-green: #2f4a2a;
  }
  * { margin: 0; padding: 0; box-sizing: border-box; }
  html, body {
    width: 1125px;
    height: 1200px;
    overflow: hidden;
    background: var(--page-bg);
    font-family: "Roboto", Arial, sans-serif;
  }
  .card {
    position: absolute;
    left: 171px;
    width: 826px;
    height: 471px;
    text-align: center;
  }
  .card--front { top: 106px; background: var(--card-dark); }
  .card--back  { top: 639px; background: var(--card-light); }

  .person-name {
    position: absolute; top: 154px; left: 0; right: 0;
    font-family: "Roboto Condensed", "Arial Narrow", sans-serif;
    font-weight: 700; font-size: 31px; line-height: 38px;
    color: var(--accent-blue);
  }
  .person-role {
    position: absolute; top: 190px; left: 0; right: 0;
    font-weight: 500; font-size: 21px; line-height: 28px;
    color: var(--accent-blue);
  }
  .dotted-rule {
    position: absolute; top: 236px; left: 351px;
    width: 124px; border-top: 1px dotted #cfcfcf;
  }
  .contact-line {
    position: absolute; left: 0; right: 0;
    font-size: 19.5px; line-height: 26px; color: var(--text-white);
  }
  .contact-line--first { top: 258px; }
  .contact-line--second { top: 284px; }

  .brand {
    position: absolute; top: 182px; left: 0; right: 0;
    display: flex; align-items: center; justify-content: center; gap: 18px;
  }
  .brand-mark {
    width: 54px; height: 54px; border-radius: 50%;
    background: var(--logo-ink);
  }
  .brand-name {
    font-family: "Roboto Condensed", "Arial Narrow", sans-serif;
    font-weight: 700; font-size: 52px; letter-spacing: 1px;
    color: var(--logo-ink);
  }
  .tagline {
    position: absolute; top: 348px; left: 0; right: 0;
    font-size: 20.5px; line-height: 28px; color: var(--text-grey);
  }
  .services-heading {
    position: absolute; top: 376px; left: 77px; right: 68px;
    display: flex; align-items: center; gap: 3px;
    font-size: 20.5px; line-height: 28px; color: var(--accent-blue);
  }
  .services-heading::before,
  .services-heading::after {
    content: ""; flex: 1; height: 1px;
  }
  .services-heading::before { background: linear-gradient(to right, rgba(47,74,42,0), var(--rule-green)); }
  .services-heading::after  { background: linear-gradient(to left, rgba(47,74,42,0), var(--rule-green)); }
  .services-list {
    position: absolute; top: 402px; left: 0; right: 0;
    font-size: 20.5px; line-height: 28px; color: var(--text-grey);
  }
  .services-list .sep { color: var(--accent-blue); margin: 0 7px; }
</style>
</head>
<body>
  <section class="card card--front">
    <h1 class="person-name">Gordon Pelliway</h1>
    <p class="person-role">Company Director</p>
    <div class="dotted-rule"></div>
    <p class="contact-line contact-line--first">04 58 736 042 | gord@trevinpave.com.au</p>
    <p class="contact-line contact-line--second">www.trevinpave.com.au</p>
  </section>

  <section class="card card--back">
    <div class="brand">
      <span class="brand-mark"></span>
      <span class="brand-name">TREVIN ASPHALT</span>
    </div>
    <p class="tagline">We do all aspects of Asphalt Paving.</p>
    <p class="services-heading">Specific Services</p>
    <p class="services-list">Driveways<span class="sep">•</span>Carparks &amp; sub-divisions<span class="sep">•</span>All Roads<span class="sep">•</span>Repairs &amp; Maintenance.</p>
  </section>
</body>
</html>
```